Ad Banner for Insight Net Panel

This banner is used in "Query Harbor" web site. This web site provides a single place for all employees to ask questions related to work. There will be dedicated subject matter experts to respond to all questions. The web site also provides "Talent Atlas" where employee can see the list of all experts in the company.
1. Banner size: 940x380
2. Business background: Provides maintenance, design and engineering, construction, machinery operation, material procurement and production management services for petrochemical and refinery business
3. We would like to see designs that
- Promote the ask questions in "Query Harbor" system
- Promote that company has experts in the areas of "Maintenance and Engineering" and can be found in "Talent Atlas"
- Encourage employees to advocate himself to be an expert by sending an email to a specific email address.
- Do not include picture of real people in the banner

```html
<!DOCTYPE html>
<html lang="en">
<head>
<meta charset="utf-8">
<title>Insight Net Panel – Be an Expert</title>
<link rel="stylesheet" href="https://fonts.googleapis.com/css2?family=Montserrat:wght@600;700;800&display=swap">
<style>
  :root {
    --sky-light: #7ad6f4;
    --sky-mid: #2fb0e4;
    --sky-deep: #1688c6;
    --headline-white: #f2f4f6;
    --expert-yellow: #ffc20e;
    --button-top: #ffb62a;
    --button-bottom: #f08a00;
    --note-navy: #0d4f80;
    --helmet-yellow: #f7b500;
    --tower-grey: #8a8f96;
  }
  html, body {
    margin: 0;
    padding: 0;
    width: 1200px;
    height: 485px;
    overflow: hidden;
  }
  .banner {
    position: relative;
    width: 1200px;
    height: 485px;
    overflow: hidden;
    background:
      radial-gradient(ellipse 520px 420px at 300px 230px, var(--sky-light) 0%, var(--sky-mid) 55%, transparent 100%),
      linear-gradient(90deg, var(--sky-mid) 0%, var(--sky-deep) 100%);
    font-family: "Montserrat", Arial, sans-serif;
  }
  .hero-art {
    position: absolute;
    left: 122px;
    top: 22px;
    width: 268px;
    height: 448px;
  }
  .message {
    position: absolute;
    left: 560px;
    width: 500px;
    text-align: center;
    text-transform: uppercase;
  }
  .lead {
    top: 62px;
    margin: 0;
    font-weight: 800;
    font-size: 68px;
    line-height: 1;
    color: var(--headline-white);
    text-shadow: 0 2px 4px rgba(0, 40, 80, 0.25);
  }
  .keyword {
    top: 118px;
    margin: 0;
    font-weight: 700;
    font-size: 132px;
    line-height: 1;
    letter-spacing: -3px;
    color: var(--expert-yellow);
    text-shadow: 0 3px 6px rgba(0, 40, 80, 0.25);
  }
  .field {
    top: 240px;
    margin: 0;
    font-weight: 700;
    font-size: 41px;
    line-height: 1.08;
    color: var(--headline-white);
    text-shadow: 0 2px 4px rgba(0, 40, 80, 0.25);
  }
  .cta {
    position: absolute;
    left: 688px;
    top: 345px;
    width: 246px;
    height: 48px;
    border-radius: 4px;
    background: linear-gradient(180deg, var(--button-top), var(--button-bottom));
    box-shadow: 0 2px 5px rgba(0, 40, 80, 0.3);
    color: #fff;
    font-weight: 700;
    font-size: 19px;
    line-height: 48px;
    text-align: center;
    text-decoration: none;
    text-transform: uppercase;
  }
  .mail-note {
    top: 409px;
    margin: 0;
    font-weight: 600;
    font-size: 13px;
    line-height: 1.3;
    color: var(--note-navy);
  }
</style>
</head>
<body>
  <main class="banner">
    <svg class="hero-art" viewBox="0 0 268 448" role="img" aria-label="Illustration of a yellow hard hat with a cluster of grey skyscrapers rising out of it">
      <defs>
        <linearGradient id="heroTones" x1="0" y1="0" x2="0" y2="1">
          <stop offset="0" stop-color="var(--tower-grey)"/>
          <stop offset="0.48" stop-color="var(--tower-grey)"/>
          <stop offset="0.6" stop-color="var(--helmet-yellow)"/>
          <stop offset="1" stop-color="var(--helmet-yellow)"/>
        </linearGradient>
      </defs>
      <rect x="0" y="0" width="268" height="448" rx="18" fill="url(#heroTones)" opacity="0.9"/>
    </svg>

    <h1 class="message lead">Be an</h1>
    <p class="message keyword">Expert</p>
    <p class="message field">In Maintenance &amp;<br>Engineering</p>

    <a class="cta" href="#">Click for more</a>

    <p class="message mail-note">Or send an email at<br>info@queryharbor.com</p>
  </main>
</body>
</html>
```